Help keep hoosiers happy and at home!

We need a billboard designed for our Indiana based healthcare business called 'Willow Hearth Caregivers'. We administer a medicaid waiver program that provides support and financial aid to live in caregivers that take care of someone who would otherwise be in a nursing home or skilled nursing facility. Qualified caregivers could be eligible to receive up to 1200 dollars a month in tax free financial aid, as well as access to nursing support that helps manage any unexpected situations or changes in a care recipients condition or care routine. Our program empowers families to keep their loved ones at home and out of the nursing home. NOTE: We believe the tagline at the bottom of our logo is disproportionately small. We would like to see that tagline larger and easier to read. I look forward to seeing your design ideas!

Target Market(s)

Medicaid aged beneficiaries and caregivers.

Industry/Entity Type

Home Healthcare

Colors
0054AA
0677BA
7BADD7
CADEEF
E8F1F8

Requirements
Nice to have
• "Empowering friends and family to care for their loves ones at home. Eligible participants receive up to $15,000 a year, tax free."

```html
<!DOCTYPE html>
<html lang="en">
<head>
<meta charset="utf-8">
<title>Willow Hearth Caregivers – Billboard</title>
<link rel="stylesheet" href="https://fonts.googleapis.com/css2?family=Poppins:wght@400;500;600;700&display=swap">
<style>
  :root {
    --navy: #1c2a80;
    --navy-deep: #16226e;
    --sky: #7badd7;
    --pill: #5e93d3;
    --white: #ffffff;
    --ink: #1c2a60;
    --page: #b5b5b5;
    --photo-a: #cfe0ee;
    --photo-b: #e9dccf;
  }
  * { box-sizing: border-box; margin: 0; padding: 0; }
  html, body { width: 850px; height: 1200px; overflow: hidden; }
  body {
    background: var(--page);
    font-family: "Poppins", sans-serif;
    position: relative;
  }
  .billboard {
    position: absolute;
    left: 15px; top: 387px;
    width: 820px; height: 426px;
    background: var(--white);
    overflow: hidden;
    box-shadow: 6px 8px 10px rgba(0,0,0,.35);
  }
  .navy-field {
    position: absolute; left: 0; top: 0;
    width: 100%; height: 258px;
    background: var(--navy);
  }
  .photo-house {
    position: absolute; left: 0; top: 0;
    width: 820px; height: 426px;
  }
  .headline {
    position: absolute; left: 49px; top: 44px;
    color: var(--white);
    line-height: 1;
  }
  .headline__main {
    display: block;
    font-weight: 700;
    font-size: 56px;
    letter-spacing: 0.5px;
  }
  .headline__accent {
    display: block;
    margin-top: 2px;
    font-weight: 600;
    font-size: 44.5px;
    color: var(--sky);
  }
  .headline__accent .amp { color: var(--white); font-weight: 500; }
  .headline__sub {
    display: block;
    margin-top: 6px;
    font-weight: 600;
    font-size: 17.6px;
  }
  .offer {
    position: absolute; left: 48px; top: 206px;
    width: 464px; height: 95px;
    background: var(--pill);
    border-radius: 16px 0 0 16px;
    box-shadow: 0 6px 8px rgba(0,0,0,.28);
    color: var(--white);
  }
  .offer__lead {
    position: absolute; right: 326px; top: 15px;
    text-align: right;
    font-weight: 500;
    font-size: 15.5px;
    line-height: 1.17;
  }
  .offer__rule {
    position: absolute; top: 14px;
    width: 2px; height: 62px;
    background: var(--white);
  }
  .offer__rule--one { left: 157px; }
  .offer__rule--two { left: 325px; }
  .offer__amount {
    position: absolute; left: 175px; top: 12px;
    font-weight: 700; font-size: 35px; line-height: 1;
  }
  .offer__amount sup { font-size: 17px; vertical-align: 14px; }
  .offer__period {
    position: absolute; left: 179px; top: 53px;
    font-weight: 700; font-size: 17.5px; line-height: 1;
    color: var(--navy);
  }
  .offer__tax {
    position: absolute; left: 350px; top: 14px;
    width: 62px; text-align: center;
    font-weight: 700; font-size: 29px; line-height: 1;
  }
  .offer__free {
    position: absolute; left: 351px; top: 46px;
    width: 62px; height: 24px;
    background: var(--navy);
    font-weight: 700; font-size: 17px; line-height: 24px;
    text-align: center;
  }
  .brand {
    position: absolute; left: 48px; top: 336px;
    display: flex; align-items: center; gap: 8px;
    color: var(--navy);
    font-weight: 600; font-size: 15px; line-height: 1.15;
  }
  .brand__dot {
    width: 14px; height: 14px; border-radius: 50%;
    background: var(--navy); flex: none;
  }
  .website {
    position: absolute; right: 354px; top: 334px;
    text-align: right;
    color: var(--ink);
  }
  .website__label {
    display: block;
    font-weight: 500; font-size: 15px; letter-spacing: 0.6px; line-height: 1.2;
  }
  .website__url {
    display: block;
    font-weight: 600; font-size: 20.5px; line-height: 1.2;
    color: var(--navy);
  }
  .website__url .mid { color: var(--pill); }
</style>
</head>
<body>
  <main class="billboard">
    <div class="navy-field"></div>

    <svg class="photo-house" viewBox="0 0 820 426" role="img" aria-label="Photograph of a smiling family of four lying on the floor of a bright living room, framed in a house shape">
      <defs>
        <linearGradient id="roomTone" x1="0" y1="0" x2="1" y2="1">
          <stop offset="0" stop-color="var(--photo-a)"/>
          <stop offset="0.6" stop-color="var(--photo-b)"/>
          <stop offset="1" stop-color="#f4f2ef"/>
        </linearGradient>
      </defs>
      <polygon points="673,34 820,141 820,426 478,426 512,330 512,188 464,188" fill="url(#roomTone)"/>
      <polyline points="464,188 673,34 820,141" fill="none" stroke="var(--sky)" stroke-width="4"/>
    </svg>

    <h1 class="headline">
      <span class="headline__main">EMPOWERING</span>
      <span class="headline__accent">FRIENDS <span class="amp">&amp;</span> FAMILY</span>
      <span class="headline__sub">TO CARE FOR THEIR LOVES ONES AT HOME</span>
    </h1>

    <section class="offer">
      <p class="offer__lead">Eligible<br>participants<br>receive up to</p>
      <span class="offer__rule offer__rule--one"></span>
      <p class="offer__amount"><sup>$</sup>15,000</p>
      <p class="offer__period">A YEAR</p>
      <span class="offer__rule offer__rule--two"></span>
      <p class="offer__tax">TAX</p>
      <p class="offer__free">FREE</p>
    </section>

    <div class="brand">
      <span class="brand__dot"></span>
      <span>Willow Hearth<br>Caregivers</span>
    </div>

    <div class="website">
      <span class="website__label">visit our website</span>
      <span class="website__url">www.<span class="mid">willowhearthcare</span>.com</span>
    </div>
  </main>
</body>
</html>
```